Native Bush Healing Balms/Oils needs label/logo

Kōwhai Ripples is our name, we are a new startup business in New Zealand. Kōwhai means love in Maori. We make native bush balms, oils, tinctures, teas and do mirimiri which is a form of Maori healing. We are wanting a design for a balm label first off, however keep in mind that we will be wanting to transfer the logo across to other products, like the teas, t-shirts and even a calico tote bag! We would like it so we can edit the ingredients if possible.

We have had the 'flower/heart logo' made up to replace the 'o' in kōwhai. This we would like in a metallic electric purple/violet colour. We would like the 'kōwhai ripples' in silver. Please make sure the macron is above the last ā in kōwhai. We are open to other colour options and other styles of the flower/heart logo.

We would like the overall effect to be simple, clean, minimalist, bright. Colours we like are electric purple/violet, silver, then thinking of different colours for the different types/flavours, probably on a matte sticker. Fonts we think will suit are an italic curved/rounded font for the kōwhai and a capital font for the vibrations.

We have had a quick mock up of the labels which is attached. Also attached is a photo of my current balm and teas, and label ideas that I like. The drawings show a sticker for the lid with a safety tab.

Looking forward to seeing your wonderful designs! :)

Target Market(s)

People into natural self healing, who want traditionally made high vibrational, top end products

Industry/Entity Type

Health And Wellness

Requirements
Must have
• Silver writing on logo, or front of jar or lid.
• 'Made in Aotearoa' on jar
Nice to have
• Colours I like are hot pink, yellow, bright teal green, royal purple
Should not have
• Should not be cluttered

```html
<!DOCTYPE html>
<html lang="en">
<head>
<meta charset="utf-8">
<title>Kōwhai Ripples – Kawakawa Balm Labels</title>
<link rel="stylesheet" href="https://fonts.googleapis.com/css2?family=Josefin+Sans:ital,wght@1,400&family=Arimo:wght@700&family=Josefin+Sans:wght@300;400&display=swap">
<style>
  :root {
    --bg: #ffffff;
    --sticker: #050505;
    --jar-label: #2a1c1a;
    --label: #000000;
    --violet: #c77ee0;
    --silver: #d9d9d9;
    --silver-soft: #bdbdbd;
    --tab-text: #e6e6e6;
  }
  * { margin: 0; padding: 0; box-sizing: border-box; }
  html, body { width: 1200px; height: 548px; overflow: hidden; background: var(--bg); }
  .canvas { position: relative; width: 1200px; height: 548px; }

  .lid-sticker { position: absolute; top: 172px; width: 208px; height: 296px; }
  .lid-sticker--mark { left: 48px; }
  .lid-sticker--name { left: 288px; }
  .lid-sticker__disc {
    position: absolute; left: 0; top: 0; width: 208px; height: 208px;
    border-radius: 50%; background: var(--sticker);
    display: flex; align-items: center; justify-content: center; flex-direction: column;
  }
  .lid-sticker__ring {
    position: absolute; inset: 10px; border-radius: 50%;
    border: 2px solid var(--silver-soft);
  }
  .lid-sticker__tab {
    position: absolute; left: 92px; top: 200px; width: 24px; height: 68px;
    background: var(--sticker);
    display: flex; align-items: center; justify-content: center;
  }
  .lid-sticker__tab-text {
    writing-mode: vertical-rl; font-family: "Arimo", sans-serif; font-size: 6px;
    letter-spacing: 0.5px; color: var(--tab-text); line-height: 1.1; text-align: center;
  }
  .brand-dot {
    width: 64px; height: 64px; border-radius: 50%; background: var(--violet); margin-bottom: 12px;
  }

  .brand-name {
    font-family: "Josefin Sans", sans-serif; font-style: italic; font-weight: 400;
    text-transform: lowercase; line-height: 1; text-align: center;
  }
  .brand-name--violet { color: var(--violet); }
  .brand-name--silver { color: var(--silver); }

  .jar-label {
    position: absolute; left: 546px; top: 120px; width: 254px; height: 300px;
    background: var(--jar-label); border-radius: 6px;
    display: flex; flex-direction: column; align-items: center; padding-top: 72px;
  }
  .product-label {
    position: absolute; left: 850px; top: 206px; width: 290px; height: 224px;
    background: var(--label);
    display: flex; flex-direction: column; align-items: center; padding-top: 52px;
  }

  .product-title { margin-top: 22px; position: relative; width: 200px; text-align: center; }
  .product-title__name {
    font-family: "Arimo", sans-serif; font-weight: 700; font-size: 30px;
    color: var(--silver); letter-spacing: 0.5px; line-height: 1;
  }
  .product-title__frame {
    position: absolute; left: 0; right: 0; top: 18px; height: 26px;
    border: 1px solid var(--silver-soft); border-top: none;
  }
  .product-title__kind {
    position: relative; display: inline-block; margin-top: 8px; padding: 0 6px;
    font-family: "Josefin Sans", sans-serif; font-weight: 400; font-size: 12px;
    letter-spacing: 1.5px; color: var(--silver); background: inherit;
  }
  .jar-label .product-title__kind { background: var(--jar-label); }
  .product-label .product-title__kind { background: var(--label); }
</style>
</head>
<body>
<main class="canvas">

  <section class="lid-sticker lid-sticker--mark" aria-label="Lid sticker with brand symbol">
    <div class="lid-sticker__disc">
      <div class="lid-sticker__ring"></div>
      <span class="brand-dot"></span>
      <span class="brand-name brand-name--violet" style="font-size:20px;">kōwhai ripples</span>
    </div>
    <div class="lid-sticker__tab"><span class="lid-sticker__tab-text">HEAL THE<br>PEOPLE</span></div>
  </section>

  <section class="lid-sticker lid-sticker--name" aria-label="Lid sticker with brand name">
    <div class="lid-sticker__disc">
      <div class="lid-sticker__ring"></div>
      <span class="brand-name brand-name--violet" style="font-size:30px;">kōwhai<br>ripples</span>
    </div>
    <div class="lid-sticker__tab"><span class="lid-sticker__tab-text">HEAL THE<br>PEOPLE</span></div>
  </section>

  <section class="jar-label" aria-label="Jar front label">
    <span class="brand-name brand-name--silver" style="font-size:30px;">kōwhai<br>ripples</span>
    <div class="product-title">
      <div class="product-title__frame"></div>
      <div class="product-title__name">Kawakawa</div>
      <div class="product-title__kind">Handmade Balm</div>
    </div>
  </section>

  <section class="product-label" aria-label="Flat product label">
    <span class="brand-name brand-name--silver" style="font-size:30px;">kōwhai<br>ripples</span>
    <div class="product-title">
      <div class="product-title__frame"></div>
      <div class="product-title__name">Kawakawa</div>
      <div class="product-title__kind">Handmade Balm</div>
    </div>
  </section>

</main>
</body>
</html>
```